VELORA Business Cards

We need a business card design for VELORA (Logo Attached), a management consultancy specialized in brand & business building.

Design should be clean, smart and a touch of innnovation without being gimmicky.

The details on the card should be:
Name: Tavo Kresnidar
Title: Managing Director
Address: 42 Marrow Wharf, Tenbury Tower, Singapore 062917
Tel: +6281492736158
email: tk@veloraadvise.example
website: veloraadvise.example

For further background on corporate identity, please check www.veloraadvise.example

Dear all,

Many thanks for the submissions so far! I gave feedback to those designs that I prefer at this stage.

Overall I see that my preference goes into the direction that 'less is more' and 'simple is beautiful'

Please create uniqueness and standout by the simplicity and attraction of the overall concept and design.

Many thanks and please shout incase of questions!

Tavo

```html
<!DOCTYPE html>
<html lang="en">
<head>
<meta charset="utf-8">
<title>Velora Business Cards</title>
<link rel="stylesheet" href="https://fonts.googleapis.com/css2?family=Open+Sans:wght@400;600&display=swap">
<style>
  :root {
    --orange: #f26522;
    --charcoal: #4a4a4a;
    --ink: #3d3d3d;
    --paper: #ffffff;
    --backdrop: #f3f3f3;
    --font: "Open Sans", Arial, sans-serif;
  }
  * { box-sizing: border-box; margin: 0; padding: 0; }
  html, body { width: 1200px; height: 675px; overflow: hidden; }
  body {
    background: var(--backdrop);
    font-family: var(--font);
    display: flex;
    align-items: center;
    justify-content: center;
    gap: 44px;
  }
  .card {
    width: 520px;
    height: 300px;
    position: relative;
    box-shadow: 0 6px 18px rgba(0,0,0,0.18);
    overflow: hidden;
  }
  .card-front {
    background: var(--orange);
    display: flex;
    flex-direction: column;
    align-items: center;
    justify-content: center;
  }
  .wordmark {
    display: flex;
    align-items: center;
    gap: 10px;
    font-family: var(--font);
    font-weight: 600;
    letter-spacing: 1px;
    line-height: 1;
  }
  .wordmark-mark { flex: none; }
  .card-front .wordmark { font-size: 44px; color: var(--paper); }
  .card-front .wordmark-mark { width: 14px; height: 14px; background: var(--paper); }
  .tagline {
    margin-top: 12px;
    font-size: 10.5px;
    letter-spacing: 0.4px;
    text-transform: uppercase;
    color: var(--paper);
  }
  .card-back { background: var(--paper); }
  .card-back .wordmark {
    position: absolute;
    right: 36px;
    top: 98px;
    font-size: 27px;
    color: var(--charcoal);
    gap: 7px;
  }
  .card-back .wordmark-mark { width: 9px; height: 9px; background: var(--orange); }
  .contact {
    position: absolute;
    left: 44px;
    top: 62px;
    color: var(--ink);
  }
  .person-name { font-size: 18px; font-weight: 400; }
  .person-title { font-size: 12.5px; color: var(--orange); margin-top: 1px; }
  .address { font-size: 12.5px; line-height: 1.4; margin-top: 12px; }
  .channels { list-style: none; margin-top: 10px; font-size: 12.5px; line-height: 1.4; }
  .channels li { display: flex; align-items: center; gap: 7px; }
  .channels svg { width: 12px; height: 12px; flex: none; }
  .base-band {
    position: absolute;
    left: 0; right: 0; bottom: 0;
    height: 13px;
    display: flex;
    gap: 5px;
  }
  .band-dark { flex: 0 0 335px; background: var(--charcoal); }
  .band-tile { flex: 1; background: var(--orange); }
</style>
</head>
<body>
  <section class="card card-front" aria-label="Card front">
    <div class="wordmark"><span class="wordmark-mark" aria-hidden="true"></span>VELORA</div>
    <div class="tagline">Strategy &amp; growth advisory for modern markets</div>
  </section>

  <section class="card card-back" aria-label="Card back">
    <div class="contact">
      <div class="person-name">Tavo Kresnidar</div>
      <div class="person-title">Managing Director</div>
      <div class="address">42 Marrow Wharf<br>Tenbury Tower<br>Singapore 062917</div>
      <ul class="channels">
        <li>
          <svg viewBox="0 0 12 12" aria-hidden="true"><circle cx="6" cy="6" r="6" fill="#f26522"/><path d="M3 4.2c0-.6.6-1.2 1.2-1.2h3.6c.6 0 1.2.6 1.2 1.2v.6H7.4v-.6H4.6v.6H3zM3.6 5.4h4.8l.6 3.4H3z" fill="#fff"/></svg>
          +6281492736158
        </li>
        <li>
          <svg viewBox="0 0 12 12" aria-hidden="true"><rect width="12" height="12" rx="1.5" fill="#f26522"/><path d="M2.5 3.8h7v4.6h-7zM2.5 3.8 6 6.6 9.5 3.8" fill="none" stroke="#fff" stroke-width="0.9"/></svg>
          tk@veloraadvise.example
        </li>
        <li>
          <svg viewBox="0 0 12 12" aria-hidden="true"><circle cx="6" cy="6" r="6" fill="#f26522"/><circle cx="6" cy="6" r="3.6" fill="none" stroke="#fff" stroke-width="0.8"/><ellipse cx="6" cy="6" rx="1.5" ry="3.6" fill="none" stroke="#fff" stroke-width="0.8"/><path d="M2.4 6h7.2" stroke="#fff" stroke-width="0.8"/></svg>
          veloraadvise.example
        </li>
      </ul>
    </div>
    <div class="wordmark"><span class="wordmark-mark" aria-hidden="true"></span>VELORA</div>
    <div class="base-band" aria-hidden="true">
      <span class="band-dark"></span>
      <span class="band-tile"></span>
      <span class="band-tile"></span>
      <span class="band-tile"></span>
    </div>
  </section>
</body>
</html>
```